Flyer für ambulanten Pflegedienst
Zielgruppe
Ambulanter Pflegedienst in Gründung. Habe schon ein Logo und Text. Zielgruppe sind Pflege und Hilfsbedürftige Menschen

```html
<!DOCTYPE html>
<html lang="de">
<head>
<meta charset="utf-8">
<title>Pflege Hafen – Flyer</title>
<link href="https://fonts.googleapis.com/css2?family=Lato:wght@400;700;900&family=Jost:wght@500;600&family=Open+Sans:wght@400;600&display=swap" rel="stylesheet">
<style>
  :root{
    --blue:#2e9abf;
    --teal:#55bdb6;
    --ink:#333a3f;
    --paper:#f7fafb;
    --white:#ffffff;
    --backdrop:#e4e6e7;
  }
  *{margin:0;padding:0;box-sizing:border-box}
  html,body{width:953px;height:1200px;overflow:hidden;background:var(--backdrop)}
  .spread{position:relative;width:953px;height:1200px}
  .page{position:absolute;top:289px;width:440px;height:622px;background:var(--paper);overflow:hidden}
  .page--front{left:24px}
  .page--back{left:489px;background:var(--white)}

  /* front */
  .hero-photo{position:absolute;left:0;top:0;width:440px;height:290px;
    background:linear-gradient(120deg,#f1e7df 0%,#e2d3c7 45%,#c7b3a3 75%,#d9c3a4 100%)}
  .hero-list{position:absolute;left:26px;top:220px;list-style:none;
    font:700 15px/1.35 Lato,sans-serif;color:var(--blue);text-transform:uppercase;letter-spacing:.3px}
  .hero-list li::before{content:"• "}
  .service-band{position:absolute;left:0;top:272px;width:440px;height:170px}
  .service-list{position:absolute;left:0;top:295px;width:440px;list-style:none;text-align:center;
    font:700 12px/1.55 Lato,sans-serif;color:var(--white);text-transform:uppercase;letter-spacing:.2px}
  .service-list li::before{content:"• "}
  .service-list small{font-size:8px}
  .service-list .lower{text-transform:none}
  .caller-photo{position:absolute;left:30px;top:458px;width:150px;height:150px;border-radius:50%;
    background:radial-gradient(circle at 45% 40%,#f2ede6 0%,#d8cdbf 55%,#a88a7a 100%)}
  .contact{position:absolute;left:218px;top:462px;font-family:Jost,sans-serif;color:var(--blue)}
  .contact h2{font:600 13px/1 Jost,sans-serif;text-transform:uppercase;letter-spacing:.3px;margin-bottom:10px}
  .contact p{font:600 13.5px/22px Jost,sans-serif}

  /* back */
  .brand{position:absolute;left:50px;top:32px;display:flex;align-items:center;gap:10px}
  .brand-dot{width:34px;height:34px;border-radius:50%;background:var(--teal)}
  .brand-name{font:900 30px/1 Lato,sans-serif;color:var(--blue)}
  .top-waves{position:absolute;left:0;top:70px;width:440px;height:110px}
  .badge{position:absolute;right:26px;top:70px;width:92px;height:92px;border-radius:50%;
    background:var(--teal);border:3px solid var(--white);display:flex;align-items:center;justify-content:center;
    text-align:center;font:700 12px/1.2 Lato,sans-serif;color:var(--white);text-transform:uppercase}
  .care-photo{position:absolute;left:28px;top:152px;width:196px;height:186px;
    background:linear-gradient(135deg,#cfd8de 0%,#b9c6cf 40%,#c98a76 70%,#9aa7b3 100%)}
  .steps{position:absolute;left:238px;top:172px;list-style:none;
    font:700 13.5px/1.4 Lato,sans-serif;color:var(--blue);text-transform:uppercase}
  .steps li::before{content:"• "}
  .intro{position:absolute;left:238px;top:258px;width:182px;
    font:400 8px/10.2px "Open Sans",sans-serif;color:var(--ink)}
  .claim{position:absolute;left:28px;top:346px;width:200px;
    font:900 12.5px/15.5px Lato,sans-serif;color:var(--blue)}
  .mission{position:absolute;left:28px;top:430px;width:198px;text-align:justify;hyphens:auto;
    font:400 8px/10.2px "Open Sans",sans-serif;color:var(--ink)}
  .bottom-waves{position:absolute;left:0;bottom:0;width:440px;height:70px}
</style>
</head>
<body>
<main class="spread">

  <section class="page page--front">
    <div class="hero-photo" role="img" aria-label="Foto: Pflegerin legt lächelnd den Arm um eine ältere Dame"></div>
    <ul class="hero-list">
      <li>Grundpflege</li>
      <li>Behandlungspflege</li>
    </ul>
    <svg class="service-band" viewBox="0 0 440 170" aria-hidden="true">
      <path d="M0 30 Q220 -8 440 30 L440 132 Q220 178 0 132 Z" fill="var(--teal)"/>
      <path d="M0 40 Q220 4 440 40 L440 122 Q220 164 0 122 Z" fill="var(--blue)"/>
    </svg>
    <ul class="service-list">
      <li><span class="lower">24 Std.</span> Pflege</li>
      <li>Hauswirtschaftliche Versorgung</li>
      <li>Betreuungs- und Entlastungsleistungen <small>nach § 45 SGB</small></li>
      <li>Verhinderungspflege</li>
      <li>Alltagsbegleitung</li>
    </ul>
    <div class="caller-photo" role="img" aria-label="Foto: ältere Dame telefoniert zu Hause"></div>
    <div class="contact">
      <h2>Rufen Sie uns gerne an:</h2>
      <p>Kontakt</p>
      <p>Name</p>
      <p>Adresse</p>
      <p>Telefon</p>
      <p>Webadresse</p>
    </div>
  </section>

  <section class="page page--back">
    <div class="brand"><span class="brand-dot"></span><span class="brand-name">Pflege Hafen</span></div>
    <svg class="top-waves" viewBox="0 0 440 110" aria-hidden="true">
      <path d="M0 10 Q200 80 440 52 L440 72 Q200 104 0 34 Z" fill="var(--blue)"/>
      <path d="M0 30 Q200 100 440 70 L440 90 Q200 122 0 52 Z" fill="var(--teal)"/>
    </svg>
    <div class="badge">Wir sind<br>für Sie da!</div>
    <div class="care-photo" role="img" aria-label="Foto: Pflegerin hält die Hände einer Seniorin im Rollstuhl"></div>
    <ul class="steps">
      <li>Beratung</li>
      <li>Pflegekonzept</li>
      <li>Vertragsabschluss</li>
      <li>Pflege</li>
    </ul>
    <p class="intro">Uns liegt es am Herzen durch qualitativ hochwertige und individuelle Unterstützungsleistungen den Menschen ein selbstbestimmtes Leben zu ermöglichen. Wir setzen auf Fachkompetenz und Empathie, um sicherzustellen, dass unsere Kunden die bestmögliche medizinische Versorgung erhalten. Unsere Dienstleistung umfasst die ambulante Pflege gemäß SGB XI sowie die Behandlungspflege gemäß SGB V. Betreuungs- und Entlastungszeiten nach § 45 SGB XI um Menschen im Alltag zu unterstützen und ihre Lebensqualität zu steigern. Pflegebedürftig ist, wer aufgrund einer körperlichen, geistigen oder seelischen Krankheit bzw. Behinderung in erheblichem Umfang Hilfe bis hin zur vollumfänglichen Betreuung benötigt. Die Leistungen des Altenpflege- und Seniorenbetreuungsdienstes erstrecken sich auf die Grundpflege, Behandlungspflege, 24-Stundenpflege, ambulante Palliativ Pflege, hauswirtschaftliche Versorgung, Verhinderungspflege und Alltagsbegleitung.</p>
    <h2 class="claim">Der Altenpflege- und Seniorenbetreuungsdienst führt sämtliche Pflegeleistungen kompetent, professionell und zuverlässig aus.</h2>
    <p class="mission">Das oberste Ziel der Pflege ist die Sicherung und Verbesserung der Lebensqualität und das Bewahren des gewohnten Lebensumfelds der Pflegepersonen. Krankenhaus- und Betreuungsheimaufenthalte sollen möglichst vermieden werden. Diesem Grundgedanken liegt die Erkenntnis zu Grunde, dass in einer vertrauten Umgebung Kranke oft schneller gesünder werden und gerade ältere Menschen sich zu Hause besonders wohl und geborgen fühlen.</p>
    <svg class="bottom-waves" viewBox="0 0 440 70" aria-hidden="true">
      <path d="M0 0 Q220 30 440 40 L440 70 L0 70 Z" fill="var(--teal)"/>
      <path d="M0 18 Q220 42 440 52 L440 70 L0 70 Z" fill="var(--blue)"/>
    </svg>
  </section>

</main>
</body>
</html>
```